Update patient consent forms and contract

Objective
Redesign the existing patient contract information document to create a modern,contempory, and easy-to-understand experience for patients. The updated design should improve readability, accessibility, and overall presentation while maintaining compliance with healthcare and legal requirements.

Key Deliverables

Refreshed visual design and layout
Improved information hierarchy and readability
Modern typography and colour palette aligned with brand guidelines
Clear section headings and navigation
Print-ready and digital versions (PDF)

Include KVE Logo within patient KVE consent to treatment. Ideally this document should be portrait not landscape.
Updates

I would love a front page to be included in the document

```html
<!DOCTYPE html>
<html lang="en">
<head>
<meta charset="utf-8">
<title>Payment Option Selection &amp; Retainer Policy</title>
<link href="https://fonts.googleapis.com/css2?family=Nunito+Sans:wght@400;600;700;800;900&display=swap" rel="stylesheet">
<style>
:root{
  --navy:#17386f;
  --blue:#1f74c4;
  --ink:#222a36;
  --muted:#4a5566;
  --line:#c9d9ee;
  --soft:#eaf2fb;
  --green:#5aa23c;
  --green-soft:#f0f6ea;
  --grey-logo:#5b5f66;
  --band:#173f7e;
  --page-border:#e3e7ee;
}
*{box-sizing:border-box;margin:0;padding:0}
html,body{width:849px;height:1200px;overflow:hidden;background:#fff}
body{font-family:"Nunito Sans",Arial,sans-serif;color:var(--ink);position:relative}
.page{position:absolute;top:37px;width:388px;height:1134px;background:#fff;border:1px solid var(--page-border);overflow:hidden}
.page--payment{left:31px}
.page--retainer{left:431px;width:392px}
.corner-glow{position:absolute;right:-70px;top:-70px;width:200px;height:200px;border-radius:50%;background:radial-gradient(circle,rgba(180,214,240,.55) 0%,rgba(214,233,247,.35) 45%,rgba(255,255,255,0) 70%)}
.brand{position:absolute;left:17px;top:22px;display:flex;align-items:center;gap:10px}
.brand__mark{width:48px;height:48px;border-radius:50%;border:5px solid var(--grey-logo)}
.brand__name{font-size:26px;font-weight:600;color:var(--grey-logo);letter-spacing:1px}
.title{position:absolute;left:22px;top:85px;right:30px;display:flex;align-items:center;gap:16px;padding-bottom:10px;border-bottom:1px solid var(--blue)}
.title__icon{width:60px;height:60px;border:1.5px solid var(--blue);border-radius:50%;display:flex;align-items:center;justify-content:center;flex:none}
.title h1{font-size:23px;line-height:24px;font-weight:900;color:var(--navy);letter-spacing:.3px}
.icon{stroke:var(--blue);fill:none;stroke-width:1.6;stroke-linecap:round;stroke-linejoin:round}
.field{position:absolute;left:26px;right:28px;display:flex;align-items:flex-end;gap:4px;font-size:10px;font-weight:700}
.field span.rule{flex:1;border-bottom:1px solid #666;height:1px;margin-bottom:2px}
.welcome{position:absolute;left:22px;top:210px;width:338px;height:131px;background:var(--soft);border-radius:8px;padding:12px 18px 0 73px;font-size:9.8px;line-height:14px;color:var(--ink)}
.welcome h2{font-size:10.5px;font-weight:800;color:var(--navy);margin-bottom:5px}
.welcome p+p{margin-top:8px}
.welcome strong{color:var(--blue)}
.circle-icon{position:absolute;width:50px;height:50px;border:1.3px solid var(--blue);border-radius:50%;display:flex;align-items:center;justify-content:center;background:transparent}
.divider-label{position:absolute;left:60px;right:60px;top:364px;display:flex;align-items:center;gap:10px;font-size:10px;font-weight:700;color:var(--navy);letter-spacing:.2px}
.divider-label::before,.divider-label::after{content:"";flex:1;border-top:1px solid var(--blue)}
.card{position:absolute;left:22px;width:338px;border:1px solid var(--line);border-radius:8px;padding:13px 18px 0 73px;font-size:9.8px;line-height:13.5px;color:var(--ink)}
.card h3{font-size:10.5px;font-weight:800;color:var(--navy);letter-spacing:.2px;margin-bottom:7px}
.card p+p{margin-top:10px}
.card .num{position:absolute;left:8px;top:9px;width:15px;height:15px;border-radius:50%;background:var(--blue);color:#fff;font-size:9px;font-weight:800;display:flex;align-items:center;justify-content:center}
.card .box{position:absolute;right:12px;top:13px;width:15px;height:15px;border:1.3px solid #6c8fb8;border-radius:3px}
.card--important{background:var(--green-soft);border-color:var(--green-soft)}
.card--important h3{color:var(--green)}
.card--declare{padding-left:57px}
.sign-line{display:flex;align-items:flex-end;gap:4px;font-weight:700;margin-top:13px}
.sign-line span{border-bottom:1px solid #666;height:1px;margin-bottom:3px}
.bank{position:absolute;left:22px;top:929px;width:308px;height:84px;border:1px solid var(--line);border-radius:8px;padding:8px 10px 0 52px;font-size:9.8px;line-height:14.2px}
.bank h3{font-size:10.3px;font-weight:800;color:var(--navy);margin-bottom:1px}
.bank dl{display:grid;grid-template-columns:84px 1fr}
.bank dt{font-weight:800;color:var(--navy)}
.bank .bank-icon{position:absolute;left:10px;top:12px}
.band{position:absolute;left:0;right:0;background:var(--band);color:#fff;font-weight:600}
.band--payment{top:1032px;height:43px;padding:7px 20px;font-size:7.8px;line-height:14px}
.band--payment .row{display:flex;gap:7px;align-items:center;white-space:nowrap}
.band .sep{opacity:.5}
.specialists{position:absolute;left:22px;right:22px;top:1084px;font-size:6.8px;line-height:9.6px;color:var(--muted)}
.specialists h4{font-size:7.6px;font-weight:800;color:var(--blue);margin-bottom:4px;letter-spacing:.2px}
.specialists .cols{display:grid;grid-template-columns:repeat(3,1fr);gap:8px}
.policy{position:absolute;left:30px;right:24px;top:171px;height:796px;display:grid;grid-template-rows:52px 62px 73px 78px 85px 76px 86px 62px 59px 56px 55px 52px;list-style:none}
.policy li{position:relative;display:flex;align-items:center;border-bottom:1px solid #e1e6ed;padding-left:3px}
.policy li:last-child{border-bottom:none}
.policy .badge{position:absolute;left:-23px;top:4px;width:15px;height:15px;border-radius:50%;background:var(--blue);color:#fff;font-size:8.5px;font-weight:800;display:flex;align-items:center;justify-content:center}
.policy .ring{width:41px;height:41px;border:1.2px solid var(--blue);border-radius:50%;display:flex;align-items:center;justify-content:center;flex:none;margin-right:17px}
.policy p{font-size:9.5px;line-height:13.8px;color:var(--ink)}
.policy p b{font-weight:800;color:#111}
.locations{position:absolute;left:10px;right:10px;top:981px;height:125px;border:1px solid var(--line);border-bottom:none;border-radius:8px 8px 0 0;padding:10px 12px 0}
.locations h3{display:flex;align-items:center;gap:5px;font-size:10px;font-weight:800;color:var(--navy);margin-bottom:8px}
.locations .cols{display:grid;grid-template-columns:repeat(3,1fr);gap:6px;font-size:6.6px;line-height:10px;color:var(--ink)}
.loc__addr{display:flex;gap:4px;min-height:34px}
.loc__contact{margin-top:4px;white-space:nowrap}
.loc__contact b{color:var(--navy);font-weight:800;display:inline-block;width:11px}
.band--retainer{top:1106px;height:28px;display:flex;align-items:center;justify-content:center;font-size:8.6px;font-weight:700}
</style>
</head>
<body>

<section class="page page--payment">
  <div class="corner-glow"></div>
  <div class="brand"><span class="brand__mark"></span><span class="brand__name">KVE</span></div>

  <header class="title">
    <div class="title__icon">
      <svg class="icon" width="28" height="30" viewBox="0 0 28 30"><path d="M5 2h12l6 6v20H5z"/><path d="M17 2v6h6"/><path d="M9 13h10M9 17h10M9 21h5"/><path d="M16 26l6-7 2 2-6 7-3 1z"/></svg>
    </div>
    <h1>PAYMENT OPTION<br>SELECTION</h1>
  </header>

  <div class="field" style="top:176px">Patient Name:<span class="rule"></span></div>

  <div class="welcome">
    <div class="circle-icon" style="left:11px;top:14px">
      <svg class="icon" width="28" height="24" viewBox="0 0 28 24"><circle cx="9" cy="7" r="4"/><circle cx="19" cy="7" r="4"/><path d="M2 21c0-5 3-8 7-8s7 3 7 8z"/><path d="M12 21c0-5 3-8 7-8s7 3 7 8z"/></svg>
    </div>
    <h2>Thank you for choosing Larch Orthodontics.</h2>
    <p>To assist with managing your treatment fees, please select your preferred payment method below. If you would prefer to pay at each scheduled appointment, please advise our reception team.</p>
    <p>Please note that appointments are generally scheduled every <strong>6–8 weeks</strong>.</p>
  </div>

  <div class="divider-label">PLEASE SELECT ONE OPTION</div>

  <div class="card" style="top:390px;height:138px">
    <span class="num">1</span><span class="box"></span>
    <div class="circle-icon" style="left:11px;top:26px">
      <svg class="icon" width="26" height="20" viewBox="0 0 26 20"><rect x="1" y="2" width="24" height="16" rx="2"/><path d="M1 7h24"/><path d="M5 13h4"/></svg>
    </div>
    <h3>CREDIT CARD DIRECT DEBIT</h3>
    <p>I would like to pay via credit card direct debit.</p>
    <p>I understand that Larch Orthodontics will send me a secure PayLink payment link to enter my credit card details. The card provided will be securely stored and used as my nominated payment method for future scheduled payments relating to my treatment plan.</p>
  </div>

  <div class="card" style="top:546px;height:113px">
    <span class="num">2</span><span class="box"></span>
    <div class="circle-icon" style="left:11px;top:30px">
      <svg class="icon" width="26" height="24" viewBox="0 0 26 24"><path d="M2 8L13 2l11 6z"/><path d="M5 11v8M10 11v8M16 11v8M21 11v8"/><path d="M2 22h22"/></svg>
    </div>
    <h3>MONTHLY DIRECT BANK TRANSFER</h3>
    <p>I would like to pay via monthly direct bank transfer.</p>
    <p>I understand that I am responsible for ensuring monthly payments are made on time in accordance with my agreed payment arrangement.</p>
  </div>

  <div class="card card--important" style="top:674px;height:106px">
    <div class="circle-icon" style="left:8px;top:8px;border-color:var(--green);border-width:1.6px">
      <svg width="8" height="26" viewBox="0 0 8 26"><path d="M4 2v15" stroke="#5aa23c" stroke-width="3" stroke-linecap="round"/><circle cx="4" cy="23" r="2" fill="#5aa23c"/></svg>
    </div>
    <h3>IMPORTANT</h3>
    <p>When making direct transfer payments, please use the patient’s full name as the payment reference (for example: <b><i>Jane Doe</i></b>), rather than the account holder’s name. This ensures payments are correctly allocated to your treatment account.</p>
  </div>

  <div class="card card--declare" style="top:797px;height:116px">
    <div class="circle-icon" style="left:8px;top:8px;width:40px;height:40px">
      <svg class="icon" width="22" height="22" viewBox="0 0 22 22"><path d="M4 16L16 4l2 2L6 18l-3 1z"/><path d="M2 21h18"/></svg>
    </div>
    <h3>PATIENT DECLARATION</h3>
    <p>I have read and understood the payment options above and agree to my selected payment method.</p>
    <div class="sign-line">Signature:<span style="width:200px"></span></div>
    <div class="sign-line" style="margin-top:11px">Date:<span style="width:135px"></span></div>
  </div>

  <div class="bank">
    <svg class="icon bank-icon" width="30" height="28" viewBox="0 0 30 28"><path d="M2 9L15 2l13 7z"/><path d="M6 12v11M12 12v11M18 12v11M24 12v11"/><path d="M2 26h26"/></svg>
    <h3>OUR BANK ACCOUNT DETAILS</h3>
    <dl>
      <dt>Account Name:</dt><dd>Larch Orthodontics</dd>
      <dt>Bank:</dt><dd>Harbour Bank</dd>
      <dt>BSB:</dt><dd>000 123</dd>
      <dt>Account Number:</dt><dd>12345678</dd>
    </dl>
  </div>

  <div class="band band--payment">
    <div class="row">
      <svg width="7" height="9" viewBox="0 0 8 10"><path d="M4 10S0 5.5 0 4a4 4 0 018 0c0 1.5-4 6-4 6z" fill="#fff"/></svg>
      <span>14 Elmwood Rd, Elmwood East VIC 3100</span><span class="sep">|</span><span><b>T.</b> 03 9000 1111</span><span class="sep">|</span><span><b>F.</b> 03 9000 2222</span>
    </div>
    <div class="row"><span><b>E.</b> elmwood@larch-ortho.com.au</span><span class="sep">|</span><span><b>W.</b> larch-ortho.com.au</span></div>
  </div>

  <div class="specialists">
    <h4>REGISTERED SPECIALIST ORTHODONTISTS</h4>
    <div class="cols">
      <div>Dr Anna Hale<br>MDSc, Grad Dip Clin Dent, BDSc(Hons)</div>
      <div>Dr Tom Reyes<br>MDSc, Grad Dip Clin Dent, MOrth, BDSc</div>
      <div>Dr Sam Lowe<br>DCD, MOrth, MRACDS (Orth), BDSc (Hons)</div>
    </div>
  </div>
</section>

<section class="page page--retainer">
  <div class="corner-glow"></div>
  <div class="brand"><span class="brand__mark"></span><span class="brand__name">KVE</span></div>

  <header class="title" style="left:34px">
    <div class="title__icon">
      <svg class="icon" width="30" height="28" viewBox="0 0 30 28"><path d="M4 24V12a11 9 0 0122 0v12h-5V13a6 5 0 00-12 0v11z"/></svg>
    </div>
    <h1>OUR RETAINER<br>POLICY</h1>
  </header>

  <ol class="policy">
    <li><span class="badge">1</span><span class="ring"><svg class="icon" width="20" height="22" viewBox="0 0 20 22"><path d="M10 2l7 3v6c0 5-3 8-7 9-4-1-7-4-7-9V5z"/><path d="M7 11l2 2 4-4"/></svg></span><p>Wearing your retainers is the most important part of your orthodontic journey.</p></li>
    <li><span class="badge">2</span><span class="ring"><svg class="icon" width="20" height="22" viewBox="0 0 20 22"><path d="M6 2c-3 0-4 3-4 6 0 4 2 5 2 9s1 3 2 3 1-5 4-5 3 5 4 5 2 1 2-3 2-5 2-9c0-3-1-6-4-6-2 0-3 1-4 1S8 2 6 2z"/></svg></span><p>Teeth shifting is a part of the natural aging process just like getting wrinkles, so lifetime maintenance is crucial.</p></li>
    <li><span class="badge">3</span><span class="ring"><svg class="icon" width="22" height="22" viewBox="0 0 22 22"><rect x="2" y="9" width="10" height="5" rx="2.5" transform="rotate(-45 7 11.5)"/><rect x="10" y="8" width="10" height="5" rx="2.5" transform="rotate(-45 15 10.5)"/></svg></span><p>Healthy teeth are not meant to be glued together, they are individual units and function independently. This is normally only done for areas of weak bone and gum or damaged teeth.</p></li>
    <li><span class="badge">4</span><span class="ring"><svg class="icon" width="24" height="24" viewBox="0 0 24 24"><circle cx="12" cy="12" r="9"/><path d="M5.5 18.5l13-13"/></svg></span><p>For this reason <b>WE DO NOT ENCOURAGE THE USE</b> OF <b>‘BONDED’</b> OR <b>‘PERMANENT’ RETAINERS.</b> Instead we advocate responsible use of removable retainers to maintain your smile.</p></li>
    <li><span class="badge">5</span><span class="ring"><svg width="6" height="22" viewBox="0 0 6 22"><path d="M3 2v12" stroke="#1f74c4" stroke-width="2.6" stroke-linecap="round"/><circle cx="3" cy="19" r="1.8" fill="#1f74c4"/></svg></span><p>Permanent or bonded retainers are not actually permanent and can cause other unexpected problems after treatment is completed, such as difficulty to clean around those teeth which can cause plaque trapping and lead to localised gum and bone loss.</p></li>
    <li><span class="badge">6</span><span class="ring"><svg class="icon" width="22" height="22" viewBox="0 0 22 22"><path d="M9 13l-3 3a2.5 2.5 0 01-3.5-3.5l3-3"/><path d="M13 9l3-3a2.5 2.5 0 013.5 3.5l-3 3"/><path d="M8 8l-2-2M14 14l2 2"/></svg></span><p>They are subject to breaking frequently, which is the reason that when bonded retainers are placed, it is recommended that you still wear a removable retainer over them anyway.</p></li>
    <li><span class="badge">7</span><span class="ring"><svg class="icon" width="26" height="16" viewBox="0 0 26 16"><rect x="1" y="2" width="6" height="6" rx="2"/><rect x="7" y="2" width="6" height="6" rx="2"/><rect x="13" y="2" width="6" height="6" rx="2"/><rect x="19" y="2" width="6" height="6" rx="2"/><rect x="1" y="8" width="6" height="6" rx="2"/><rect x="7" y="8" width="6" height="6" rx="2"/><rect x="13" y="8" width="6" height="6" rx="2"/><rect x="19" y="8" width="6" height="6" rx="2"/></svg></span><p>Bonded retainers only hold the front few teeth, whereas your orthodontic treatment involved improvements of ALL your teeth. Thus, holding the front teeth only gives the back teeth a chance to move out of alignment.</p></li>
    <li><span class="badge">8</span><span class="ring"><svg class="icon" width="22" height="22" viewBox="0 0 22 22"><path d="M14 3a8 8 0 108 10A7 7 0 0114 3z"/><path d="M16 7h3M17.5 5.5v3"/></svg></span><p>The retainers we provide at Larch Orthodontics, are only worn at night and will hold ALL your teeth where they are at the end of your orthodontic treatment.</p></li>
    <li><span class="badge">9</span><span class="ring"><svg class="icon" width="22" height="22" viewBox="0 0 22 22"><circle cx="11" cy="11" r="8.5"/><path d="M11 6v5l3 2"/></svg></span><p>Even excellent retainer wear will not guarantee that the teeth will stay exactly the same forever, due to the natural ageing and bone changing processes.</p></li>
    <li><span class="badge">10</span><span class="ring"><svg class="icon" width="20" height="22" viewBox="0 0 20 22"><path d="M4 2v18M10 2v18M16 2v18"/><circle cx="4" cy="14" r="2" fill="#fff"/><circle cx="10" cy="7" r="2" fill="#fff"/><circle cx="16" cy="12" r="2" fill="#fff"/></svg></span><p>Minor alignment adjustments may be made to your retainers in the future to ensure that you remain happy with your smile.</p></li>
    <li><span class="badge">11</span><span class="ring"><svg class="icon" width="22" height="22" viewBox="0 0 22 22"><rect x="2" y="4" width="18" height="16" rx="2"/><path d="M2 9h18M7 2v4M15 2v4"/><path d="M6 13h2M10 13h2M14 13h2M6 16h2M10 16h2M14 16h2"/></svg></span><p>After 2 years of retainer reviews, further follow up care may be charged at the current office visit rate.</p></li>
    <li><span class="badge">12</span><span class="ring"><svg class="icon" width="22" height="22" viewBox="0 0 22 22"><circle cx="11" cy="11" r="9"/><path d="M14 7.5c-1-1-5-1.5-5.5.8S14 10 14 12.6 10 16 8 14.5M11 5v12"/></svg></span><p>Lost or broken retainers will incur a fee<br>for replacement or repair.</p></li>
  </ol>

  <div class="locations">
    <h3><svg width="10" height="13" viewBox="0 0 10 13"><path d="M5 13S0 7 0 5a5 5 0 0110 0c0 2-5 8-5 8z" fill="#1f74c4"/><circle cx="5" cy="5" r="1.8" fill="#fff"/></svg>OUR LOCATIONS</h3>
    <div class="cols">
      <div>
        <div class="loc__addr"><svg class="icon" width="8" height="10" viewBox="0 0 8 10"><path d="M4 9S1 5.5 1 4a3 3 0 016 0c0 1.5-3 5-3 5z"/></svg><span>14 Elmwood Rd,<br>Elmwood East VIC 3100</span></div>
        <div class="loc__contact"><b>T.</b> 03 9000 1111<br><b>F.</b> 03 9000 2222<br><b>E.</b> elmwood@larch-ortho.com.au</div>
      </div>
      <div>
        <div class="loc__addr"><svg class="icon" width="8" height="10" viewBox="0 0 8 10"><path d="M4 9S1 5.5 1 4a3 3 0 016 0c0 1.5-3 5-3 5z"/></svg><span>8 Hilltop Rise,<br>Northvale VIC 3200<br>(Cnr Grove Street)</span></div>
        <div class="loc__contact"><b>T.</b> 03 9000 3333<br><b>F.</b> 03 9000 4444<br><b>E.</b> northvale@larch-ortho.com.au</div>
      </div>
      <div>
        <div class="loc__addr"><svg class="icon" width="8" height="10" viewBox="0 0 8 10"><path d="M4 9S1 5.5 1 4a3 3 0 016 0c0 1.5-3 5-3 5z"/></svg><span>52 Parker Street,<br>Westbrook VIC 3300</span></div>
        <div class="loc__contact"><b>T.</b> 03 9000 5555<br><b>F.</b> 03 9000 6666<br><b>E.</b> westbrook@larch-ortho.com.au</div>
      </div>
    </div>
  </div>

  <div class="band band--retainer">W. larch-ortho.com.au</div>
</section>

</body>
</html>
```